Eye surgeon needs a presentation folder and a business card for his practice manager. Logo alread...

I need a folder to put papers in when I am scheduling patients for surgery. The information is general, such as costs, consent forms etc. The folder is designed to give the patient these papers in a neat manner. The cover of the folder needs to use my brand and perhaps create some interest when it is sitting on their kitchen bench with visitors and family. I'll attach a typical template for a folder. It needs to be stylish, classic and professional, as I am about to operate on the person's eye. <br/>I would like my logo included. I'll also attach a photo which is on my website which might work to wrap around the folder. The website address is raybelford.com.au and you can see the way the image is used there on most of the pages as a banner. My profile photo could possibly used as well. Perhaps on the back, but if it looks strange then that is not necessary. The contact information need not be on the folder. Just Dr Ray Belford, Ophthalmic Surgeon. Finally, our brand slogan is. "The world's a beautiful place, see it clearly". This could also be on it. Again, this all needs to be professional looking. <br/>I've attached all our previous design jobs, 2 profile pictures, and the image that I think would work. Please also look at the website. <br/><br/>The second part of the project is to create a business card for my practice manager. Her name is Miriam Holtby<br/>It should include<br/>Miriam Holtby (BCom)<br/>Practice Manager for Dr Ray Belford<br/>Ophthalmic Surgeon <br/><br/>Then all the details which are on our current business card<br/><br/><br/><br/><br/>

Contact Information for Business Card

Just match the business cards I already have, but use the details above

Colors

Designer to choose colors to be used in the design.

```html
<!DOCTYPE html>
<html lang="en">
<head>
<meta charset="utf-8">
<title>Dr Ray Belford – Presentation Folder Dieline</title>
<link rel="stylesheet" href="https://fonts.googleapis.com/css2?family=Arimo:wght@400;700&family=Open+Sans:wght@300;400;600;700&display=swap">
<style>
  :root {
    --paper: #ffffff;
    --frame: #6d6d6d;
    --dieline: #2b2b2b;
    --flap-blue: #3a95d6;
    --flap-blue-deep: #2f84c6;
    --brand-blue: #1f86c8;
    --brand-navy: #1c3550;
    --photo-top: #626a74;
    --photo-upper: #8a8072;
    --photo-warm: #cf9848;
    --photo-lower: #6e5236;
    --photo-deep: #312e2b;
    --photo-base: #16191d;
    --label-magenta: #d4148c;
    --white: #ffffff;
  }
  * { margin: 0; padding: 0; box-sizing: border-box; }
  html, body {
    width: 1200px; height: 861px; overflow: hidden;
    background: var(--paper);
    font-family: "Open Sans", Arial, sans-serif;
  }
  .sheet {
    position: relative; width: 1200px; height: 861px;
    border: 1px solid var(--frame);
    background: var(--paper);
  }
  .dieline { position: absolute; inset: 0; }
  .overlay { position: absolute; }

  .brand-lockup { display: flex; align-items: flex-start; gap: 6px; }
  .brand-mark { border-radius: 50%; background: var(--brand-blue); flex: none; }
  .brand-name { color: var(--brand-blue); font-weight: 600; line-height: 1; white-space: nowrap; }
  .brand-title { font-weight: 700; line-height: 1.2; white-space: nowrap; }
  .brand-quals { font-weight: 400; line-height: 1.2; white-space: nowrap; }

  .front-lockup { left: 738px; top: 370px; }
  .front-lockup .brand-mark { width: 30px; height: 30px; margin-top: 4px; }
  .front-lockup .brand-name { font-size: 20px; }
  .front-lockup .brand-title { font-size: 8px; margin-top: 3px; color: var(--brand-navy); }
  .front-lockup .brand-quals { font-size: 7px; color: var(--brand-navy); }

  .back-lockup { left: 246px; top: 587px; }
  .back-lockup .brand-mark { width: 22px; height: 22px; margin-top: 2px; }
  .back-lockup .brand-name { font-size: 14px; }
  .back-lockup .brand-title { font-size: 7px; margin-top: 2px; color: var(--white); }
  .back-lockup .brand-quals { font-size: 6px; color: var(--white); }

  .portrait {
    left: 295px; top: 515px; width: 66px; height: 66px; border-radius: 50%;
    background: #d9c2b0;
    border: 2px solid var(--white);
  }

  .slogan {
    right: 66px; top: 515px; text-align: right;
    color: var(--white); font-family: "Arimo", Arial, sans-serif;
    font-weight: 400; font-size: 27px; line-height: 32px; letter-spacing: -0.2px;
  }
  .front-url {
    right: 66px; top: 600px; color: var(--white); font-family: "Arimo", Arial, sans-serif;
    font-size: 14px;
  }
  .back-address {
    left: 526px; top: 581px; color: var(--white); font-style: normal;
    font-family: "Arimo", Arial, sans-serif; font-size: 9px; line-height: 12px;
  }
  .back-address .street { font-weight: 700; }
  .back-address .web { font-weight: 400; font-size: 10px; }

  .view-label {
    color: var(--label-magenta); font-family: "Arimo", Arial, sans-serif;
    font-size: 25px; font-weight: 400; white-space: nowrap;
  }
  .view-label--back { left: 322px; top: 746px; }
  .view-label--front { left: 853px; top: 697px; }
</style>
</head>
<body>
<main class="sheet">
  <svg class="dieline" width="1200" height="861" viewBox="0 0 1200 861">
    <defs>
      <linearGradient id="coverTones" x1="0" y1="33" x2="0" y2="685" gradientUnits="userSpaceOnUse">
        <stop offset="0" stop-color="var(--photo-top)"/>
        <stop offset="0.32" stop-color="var(--photo-upper)"/>
        <stop offset="0.58" stop-color="var(--photo-warm)"/>
        <stop offset="0.7" stop-color="var(--photo-lower)"/>
        <stop offset="0.84" stop-color="var(--photo-deep)"/>
        <stop offset="1" stop-color="var(--photo-base)"/>
      </linearGradient>
      <linearGradient id="flapShade" x1="0" y1="0" x2="1" y2="1">
        <stop offset="0" stop-color="var(--flap-blue)"/>
        <stop offset="1" stop-color="var(--flap-blue-deep)"/>
      </linearGradient>
    </defs>

    <path class="side-flap" d="M186 55 L186 643 L90 643 Q28 643 28 581 L28 117 Q28 55 90 55 Z"
          fill="url(#flapShade)" stroke="var(--dieline)" stroke-width="1"/>
    <path class="pocket-flap" d="M228 685 L658 685 L658 780 Q658 840 598 840 L288 840 Q228 840 228 780 Z"
          fill="url(#flapShade)" stroke="var(--dieline)" stroke-width="1"/>

    <path role="img" aria-label="Wrap-around sunset photograph over the ocean with a fishing rod, across back and front covers"
          d="M207 33 L1171 33 L1171 663 L678 663 L658 685 L228 685 L186 643 L186 55 Z"
          fill="url(#coverTones)" stroke="var(--dieline)" stroke-width="1"/>

    <g class="fold-lines" stroke="var(--dieline)" stroke-width="0.8" opacity="0.8">
      <line x1="207" y1="33" x2="207" y2="663"/>
      <line x1="678" y1="33" x2="678" y2="663"/>
      <line x1="698" y1="33" x2="698" y2="663"/>
    </g>
  </svg>

  <div class="overlay portrait" role="img" aria-label="Round profile portrait of the surgeon"></div>

  <div class="overlay brand-lockup back-lockup">
    <span class="brand-mark"></span>
    <div>
      <div class="brand-name">Dr Ray Belford</div>
      <div class="brand-title">Ophthalmic Surgeon</div>
      <div class="brand-quals">MBBS (Hons) MMed FRANZCO</div>
    </div>
  </div>

  <address class="overlay back-address">
    <div class="street">24 Harbour Rd, Claremont</div>
    <div class="street">Western Australia 6010</div>
    <div class="web">www. raybelford.com.au</div>
  </address>

  <div class="overlay brand-lockup front-lockup">
    <span class="brand-mark"></span>
    <div>
      <div class="brand-name">Dr Ray Belford</div>
      <div class="brand-title">Ophthalmic Surgeon</div>
      <div class="brand-quals">MBBS (Hons) MMed FRANZCO</div>
    </div>
  </div>

  <p class="overlay slogan">The world's a beautiful<br>place, see it clearly</p>
  <p class="overlay front-url">raybelford.com.au</p>

  <p class="overlay view-label view-label--back">open file view_Back</p>
  <p class="overlay view-label view-label--front">open file view_front</p>
</main>
</body>
</html>
```